Business card for Eyelash extension salon in Beverly Hills,California USA

We need new business card for our salon in Beverly Hills. The salon name is 'Lumarra' . We would like to have...Business name: Lumarra Name of person: will provide later Address 6128 N.Corbel Ridge Blvd Beverly Hills , CA 90210 Phone: will provide later (Text only) Web: www.lumarrastudio-example.com Pictogrid icon, Friendvale icon follow us for seasonal campaign and news @lumarrastudioexample Design should look elegant, high-end, clean, simple, cohesive with my brand. Please refer my brand board. Business name color will be metallic bronzy color. Im thinking grey background or white background. Thanks

Target Market(s)

25-35. Gender neutral. People who are in Entertainment business industry.
This is High-end Eyelash extension salon in Beverly Hills

Industry/Entity Type

Beauty Salon

Contact Information for Business Card

Business name: Lumarra
Name of person: will provide later
Address 6128 N.Corbel Ridge Blvd Beverly Hills , CA 90210
Phone: will provide later (Text only)
Web: www.lumarrastudio-example.com
Pictogrid icon, Friendvale icon
follow us for seasonal campaign and news @lumarrastudioexample

Requirements
Must have
• Beautiful, elegant, clean and simple look but very attractive and modern
Should not have
• We don't like too clutter, too busy designs.

```html
<!DOCTYPE html>
<html lang="en">
<head>
<meta charset="utf-8">
<title>Lumarra Business Card</title>
<link href="https://fonts.googleapis.com/css2?family=Montserrat:wght@400;500;700&display=swap" rel="stylesheet">
<style>
  :root {
    --bronze: #8b6a54;
    --bronze-band: #8f7060;
    --ink-grey: #6e6e6e;
    --rule-grey: #b9b9b9;
    --card-white: #ffffff;
    --card-grey: #9d9d9d;
    --page: #ecebe8;
    --on-grey: #ffffff;
  }
  * { margin: 0; padding: 0; box-sizing: border-box; }
  html, body { width: 1200px; height: 960px; overflow: hidden; }
  body {
    background: var(--page);
    font-family: "Montserrat", sans-serif;
    position: relative;
  }
  .card {
    position: absolute;
    left: 250px;
    width: 700px;
    height: 400px;
    overflow: hidden;
    box-shadow: 0 2px 10px rgba(0,0,0,0.12);
  }
  .card--front { top: 60px; background: var(--card-white); }
  .card--back { top: 500px; }

  /* Front */
  .front-brand {
    position: absolute;
    left: 40px; top: 110px;
    width: 330px;
    text-align: center;
    color: var(--bronze);
  }
  .brand-name {
    font-weight: 400;
    font-size: 66px;
    letter-spacing: 2px;
    line-height: 1;
  }
  .brand-place {
    margin-top: 18px;
    font-size: 12px;
    letter-spacing: 5px;
    text-transform: uppercase;
    padding-left: 80px;
  }
  .divider {
    position: absolute;
    left: 395px; top: 70px;
    width: 1px; height: 210px;
    background: var(--rule-grey);
  }
  .contact {
    position: absolute;
    left: 425px; top: 82px;
    color: var(--ink-grey);
  }
  .person-name {
    font-weight: 700;
    font-size: 27px;
    color: var(--bronze);
    letter-spacing: 0.5px;
  }
  .person-role {
    font-size: 16px;
    margin-top: 4px;
    letter-spacing: 0.5px;
  }
  .address {
    margin-top: 30px;
    font-size: 17px;
    line-height: 1.35;
    font-style: normal;
  }
  .contact-line {
    display: flex;
    align-items: center;
    gap: 10px;
    font-size: 17px;
    margin-top: 8px;
  }
  .contact-line:first-of-type { margin-top: 16px; }
  .contact-line svg { width: 18px; height: 18px; flex: none; }
  .band {
    position: absolute;
    left: 0; bottom: 0;
    width: 100%; height: 56px;
    background: var(--bronze-band);
  }

  /* Back */
  .back-surface {
    position: absolute; inset: 0;
    background: linear-gradient(160deg, #a6a6a6, #959595);
  }
  .back-content {
    position: absolute; inset: 0;
    color: var(--on-grey);
    text-align: center;
    padding-top: 70px;
  }
  .back-content .brand-name { font-size: 72px; }
  .back-content .brand-place { padding-left: 0; margin-top: 14px; }
  .socials {
    display: flex;
    justify-content: center;
    gap: 26px;
    margin-top: 34px;
    font-size: 13px;
    letter-spacing: 0.5px;
  }
  .social { display: flex; align-items: center; gap: 7px; }
  .social-dot {
    width: 22px; height: 22px;
    border: 1.5px solid var(--on-grey);
    border-radius: 50%;
  }
  .follow {
    margin-top: 18px;
    font-size: 17px;
    letter-spacing: 0.3px;
  }
  .handle {
    margin-top: 4px;
    font-size: 17px;
  }
</style>
</head>
<body>

<section class="card card--front" aria-label="Business card front">
  <div class="front-brand">
    <div class="brand-name">Lumarra</div>
    <div class="brand-place">Beverly Hills</div>
  </div>
  <div class="divider"></div>
  <div class="contact">
    <h1 class="person-name">Marisol Venn</h1>
    <p class="person-role">Fashion Marketing</p>
    <address class="address">6128 N.Corbel Ridge Blvd<br>Beverly Hills , CA 90210</address>
    <p class="contact-line">
      <svg viewBox="0 0 24 24" aria-hidden="true"><path fill="#8b6a54" d="M6.6 10.8a15.1 15.1 0 0 0 6.6 6.6l2.2-2.2c.3-.3.7-.4 1-.2 1.1.4 2.3.6 3.6.6.6 0 1 .4 1 1V20c0 .6-.4 1-1 1A17 17 0 0 1 3 4c0-.6.4-1 1-1h3.5c.6 0 1 .4 1 1 0 1.3.2 2.5.6 3.6.1.3 0 .7-.2 1z"/></svg>
      1 123 123 1234
    </p>
    <p class="contact-line">
      <svg viewBox="0 0 24 24" aria-hidden="true" fill="none" stroke="#8b6a54" stroke-width="1.6"><circle cx="12" cy="12" r="9"/><ellipse cx="12" cy="12" rx="4" ry="9"/><path d="M3 12h18M4.5 7.5h15M4.5 16.5h15"/></svg>
      www.lumarrastudio-example.com
    </p>
  </div>
  <div class="band" role="img" aria-label="Bronze band with a fine diamond lattice pattern"></div>
</section>

<section class="card card--back" aria-label="Business card back">
  <div class="back-surface" role="img" aria-label="Soft grey background with a faint square grid pattern"></div>
  <div class="back-content">
    <div class="brand-name">Lumarra</div>
    <div class="brand-place">Beverly Hills</div>
    <div class="socials">
      <span class="social"><span class="social-dot"></span>Friendvale</span>
      <span class="social"><span class="social-dot"></span>Pictogrid</span>
    </div>
    <p class="follow">Follow Us For Seasonal Campaign News</p>
    <p class="handle">@lumarrastudioexample</p>
  </div>
</section>

</body>
</html>
```